World travel poster - I want to remember where I've been!

I would like a poster for me to print and keep in my home as a record of my world travels. It must look like a mechanical sign in an airport (see picture for example) However I am flexible with exact layout, if you'd like to add images used to enhance poster etc. I have also uploaded some pictures from my travels if you would like to use some or all of them. They are named according to location.

Poster must include:
USA 2003
Malaysia 2006
Thailand 2007
Italy 2009
India, Vietnam, Hong Kong 2010
Bali 2011
Malaysia 2012
Singapore 2012
Vietnam, Cambodia, Laos 2013
Europe 2015

and the quote:

"The world is a book and those who do not travel read only one page."
― Corwin of Veldmarsh
Updates

Hi there. I have uploaded some photos of my travels to possibly use in my poster. They are named according to location. I haven't decided if I prefer the originial layout or with images, so please post both for me to consider. Thanks so much for your time to consider my project.

Target Market(s)

Something to catch the eye of visitors and remind me of my adventures.
A classic piece that is a conversation starter.

Industry/Entity Type

Airport

Font styles to use
Other font styles liked:
• Airport mechanical font

Requirements
Must have
• Some lettering like a mechanical airport board (see image attached for example).
Dimensions that are easy to print - either A3, or a long/narrow poster.
Nice to have
• A splash of colour or an image, maybe the words 'arrivals' or 'departures'

Use of some of my pictures if it doesn't look too busy.
Should not have
• Anything too over the top.

```html
<!DOCTYPE html>
<html lang="en">
<head>
<meta charset="utf-8">
<title>Departures – Travel Board</title>
<link rel="stylesheet" href="https://fonts.googleapis.com/css2?family=Montserrat:wght@600;700&family=Roboto:wght@700&family=Raleway:wght@300;700&display=swap">
<style>
  :root {
    --bg: #2f2f30;
    --flap-top: #3c3c3d;
    --flap-bottom: #1f1f20;
    --flap-edge: #111;
    --dash-top: #8a8a8c;
    --dash-bottom: #5c5c5e;
    --ink: #f4f4f4;
    --accent: #ffcb05;
    --muted: #c9c9c9;
  }
  * { margin: 0; padding: 0; box-sizing: border-box; }
  html, body { width: 848px; height: 1200px; overflow: hidden; background: var(--bg); }
  .poster { position: relative; width: 848px; height: 1200px; background: var(--bg); }

  .header { position: absolute; left: 42px; top: 30px; display: flex; align-items: center; gap: 22px; }
  .header-plane { width: 72px; height: 40px; }
  .header-title {
    font-family: "Montserrat", sans-serif; font-weight: 700; font-size: 34px;
    letter-spacing: 5px; color: var(--accent);
  }

  .board { position: absolute; left: 42px; top: 112px; display: flex; flex-direction: column; gap: 18px; }
  .board-row { display: flex; align-items: center; gap: 4px; height: 47px; }

  .flap {
    position: relative; width: 41px; height: 47px; border-radius: 4px;
    background: linear-gradient(to bottom, var(--flap-top) 0%, #2c2c2d 49%, var(--flap-bottom) 51%, #262627 100%);
    border: 1px solid var(--flap-edge);
    box-shadow: inset 0 1px 0 rgba(255,255,255,0.12);
    display: flex; align-items: center; justify-content: center;
    font-family: "Roboto", sans-serif; font-weight: 700; font-size: 33px; color: var(--ink);
  }
  .flap::after {
    content: ""; position: absolute; left: 0; right: 0; top: 50%; height: 2px;
    margin-top: -1px; background: rgba(0,0,0,0.75);
  }
  .flap--year { color: var(--accent); }
  .flap--dash {
    background: linear-gradient(to bottom, var(--dash-top) 0%, #77777a 49%, var(--dash-bottom) 51%, #6a6a6c 100%);
  }

  .flag {
    width: 85px; height: 51px; margin-left: 4px; border-radius: 3px;
    border: 1px solid var(--flap-edge);
  }
  .flag--usa { background: linear-gradient(135deg, #2b3f8c 0 38%, #d52b2b 38% 55%, #f2f2f2 55% 70%, #d52b2b 70%); }
  .flag--malaysia { background: linear-gradient(135deg, #1f3a8f 0 40%, #d0312d 40% 60%, #f2f2f2 60% 75%, #d0312d 75%); }
  .flag--thailand { background: linear-gradient(to bottom, #c8242b 0 17%, #f2f2f2 17% 33%, #2b2f6b 33% 67%, #f2f2f2 67% 83%, #c8242b 83%); }
  .flag--italy { background: linear-gradient(to right, #1f9a48 0 33%, #f2f2f2 33% 67%, #d1343a 67%); }
  .flag--india { background: linear-gradient(to bottom, #f29a2e 0 33%, #f2f2f2 33% 67%, #1b8a3a 67%); }
  .flag--vietnam { background: radial-gradient(circle at 50% 50%, #ffd84a 0 18%, #d6262c 19%); }
  .flag--hongkong { background: radial-gradient(circle at 50% 50%, #f2f2f2 0 22%, #d6262c 23%); }
  .flag--bali { background: radial-gradient(circle at 50% 50%, #4a7bc4 0 18%, #e8a030 19%); }
  .flag--singapore { background: linear-gradient(to bottom, #e02b35 0 50%, #f2f2f2 50%); }
  .flag--laos { background: linear-gradient(to bottom, #d12b33 0 25%, #26378f 25% 75%, #d12b33 75%); }
  .flag--cambodia { background: linear-gradient(to bottom, #2b3f8c 0 25%, #d6262c 25% 75%, #2b3f8c 75%); }
  .flag--europe { background: radial-gradient(circle at 50% 50%, #1f3a8f 0 25%, #e8c84a 26% 30%, #1f3a8f 31%); }

  .quote {
    position: absolute; left: 42px; top: 918px; width: 770px;
    font-family: "Raleway", sans-serif; font-weight: 300; font-size: 44px;
    line-height: 1.18; color: var(--muted);
  }
  .quote-strong { font-weight: 700; color: var(--accent); }
  .quote-author {
    position: absolute; left: 42px; top: 1146px;
    font-family: "Raleway", sans-serif; font-weight: 300; font-size: 17px; color: var(--muted);
  }
</style>
</head>
<body>
<main class="poster">
  <header class="header">
    <svg class="header-plane" viewBox="0 0 72 40" aria-hidden="true">
      <path fill="#ffcb05" d="M4 28 L10 26 L16 30 L26 27 L16 8 L22 6 L38 24 L58 18 C66 16 70 19 68 22 C66 25 60 27 52 29 L14 38 Z"/>
    </svg>
    <h1 class="header-title">DEPARTURES</h1>
  </header>

  <section class="board" aria-label="Travel history">
    <div class="board-row">
      <span class="flap">U</span><span class="flap">S</span><span class="flap">A</span>
      <span class="flap flap--dash">–</span>
      <span class="flap flap--year">2</span><span class="flap flap--year">0</span><span class="flap flap--year">0</span><span class="flap flap--year">3</span>
      <span class="flag flag--usa" role="img" aria-label="Flag of the USA"></span>
    </div>
    <div class="board-row">
      <span class="flap">M</span><span class="flap">A</span><span class="flap">L</span><span class="flap">A</span><span class="flap">Y</span><span class="flap">S</span><span class="flap">I</span><span class="flap">A</span>
      <span class="flap flap--dash">–</span>
      <span class="flap flap--year">2</span><span class="flap flap--year">0</span><span class="flap flap--year">0</span><span class="flap flap--year">6</span>
      <span class="flag flag--malaysia" role="img" aria-label="Flag of Malaysia"></span>
    </div>
    <div class="board-row">
      <span class="flap">T</span><span class="flap">H</span><span class="flap">A</span><span class="flap">I</span><span class="flap">L</span><span class="flap">A</span><span class="flap">N</span><span class="flap">D</span>
      <span class="flap flap--dash">–</span>
      <span class="flap flap--year">2</span><span class="flap flap--year">0</span><span class="flap flap--year">0</span><span class="flap flap--year">7</span>
      <span class="flag flag--thailand" role="img" aria-label="Flag of Thailand"></span>
    </div>
    <div class="board-row">
      <span class="flap">I</span><span class="flap">T</span><span class="flap">A</span><span class="flap">L</span><span class="flap">Y</span>
      <span class="flap flap--dash">–</span>
      <span class="flap flap--year">2</span><span class="flap flap--year">0</span><span class="flap flap--year">0</span><span class="flap flap--year">9</span>
      <span class="flag flag--italy" role="img" aria-label="Flag of Italy"></span>
    </div>
    <div class="board-row">
      <span class="flap">I</span><span class="flap">N</span><span class="flap">D</span><span class="flap">I</span><span class="flap">A</span><span class="flap">,</span><span class="flap">V</span><span class="flap">I</span><span class="flap">E</span><span class="flap">T</span><span class="flap">N</span><span class="flap">A</span><span class="flap">M</span>
      <span class="flag flag--india" role="img" aria-label="Flag of India"></span>
      <span class="flag flag--vietnam" role="img" aria-label="Flag of Vietnam"></span>
    </div>
    <div class="board-row">
      <span class="flap">&amp;</span>
      <span class="flap flap--dash">–</span>
      <span class="flap">H</span><span class="flap">O</span><span class="flap">N</span><span class="flap">G</span><span class="flap">K</span><span class="flap">O</span><span class="flap">N</span><span class="flap">G</span>
      <span class="flap flap--dash">–</span>
      <span class="flap flap--year">2</span><span class="flap flap--year">0</span><span class="flap flap--year">1</span><span class="flap flap--year">0</span>
      <span class="flag flag--hongkong" role="img" aria-label="Flag of Hong Kong"></span>
    </div>
    <div class="board-row">
      <span class="flap">B</span><span class="flap">A</span><span class="flap">L</span><span class="flap">I</span>
      <span class="flap flap--dash">–</span>
      <span class="flap flap--year">2</span><span class="flap flap--year">0</span><span class="flap flap--year">1</span><span class="flap flap--year">1</span>
      <span class="flag flag--bali" role="img" aria-label="Flag of Bali"></span>
    </div>
    <div class="board-row">
      <span class="flap">M</span><span class="flap">A</span><span class="flap">L</span><span class="flap">A</span><span class="flap">Y</span><span class="flap">S</span><span class="flap">I</span><span class="flap">A</span>
      <span class="flap flap--dash">–</span>
      <span class="flap flap--year">2</span><span class="flap flap--year">0</span><span class="flap flap--year">1</span><span class="flap flap--year">2</span>
      <span class="flag flag--malaysia" role="img" aria-label="Flag of Malaysia"></span>
    </div>
    <div class="board-row">
      <span class="flap">S</span><span class="flap">I</span><span class="flap">N</span><span class="flap">G</span><span class="flap">A</span><span class="flap">P</span><span class="flap">O</span><span class="flap">R</span><span class="flap">E</span>
      <span class="flap flap--dash">–</span>
      <span class="flap flap--year">2</span><span class="flap flap--year">0</span><span class="flap flap--year">1</span><span class="flap flap--year">2</span>
      <span class="flag flag--singapore" role="img" aria-label="Flag of Singapore"></span>
    </div>
    <div class="board-row">
      <span class="flap">V</span><span class="flap">I</span><span class="flap">E</span><span class="flap">T</span><span class="flap">N</span><span class="flap">A</span><span class="flap">M</span><span class="flap">,</span><span class="flap">L</span><span class="flap">A</span><span class="flap">O</span><span class="flap">S</span>
      <span class="flag flag--vietnam" role="img" aria-label="Flag of Vietnam"></span>
      <span class="flag flag--laos" role="img" aria-label="Flag of Laos"></span>
    </div>
    <div class="board-row">
      <span class="flap">&amp;</span>
      <span class="flap flap--dash">–</span>
      <span class="flap">C</span><span class="flap">A</span><span class="flap">M</span><span class="flap">B</span><span class="flap">O</span><span class="flap">D</span><span class="flap">I</span><span class="flap">A</span>
      <span class="flap flap--dash">–</span>
      <span class="flap flap--year">2</span><span class="flap flap--year">0</span><span class="flap flap--year">1</span><span class="flap flap--year">3</span>
      <span class="flag flag--cambodia" role="img" aria-label="Flag of Cambodia"></span>
    </div>
    <div class="board-row">
      <span class="flap">E</span><span class="flap">U</span><span class="flap">R</span><span class="flap">O</span><span class="flap">P</span><span class="flap">E</span>
      <span class="flap flap--dash">–</span>
      <span class="flap flap--year">2</span><span class="flap flap--year">0</span><span class="flap flap--year">1</span><span class="flap flap--year">5</span>
      <span class="flag flag--europe" role="img" aria-label="Flag of Europe"></span>
    </div>
  </section>

  <blockquote class="quote">
    The world is a book and those who do not travel read <span class="quote-strong">only one page.</span>
  </blockquote>
  <p class="quote-author">- Corwin of Veldmarsh</p>
</main>
</body>
</html>
```